Super elegant, crisp & clean Business card design required

We recently upgraded our branding - which is on our website - tavorelstudio.com

I would like a simple, yet elegant, clean business card design please.

The font of my logo is Cinzel - and because of the natural colour - it's best to have this on a black background.

I would like to have the back of the business card - with simply my logo.

PLEASE DO NOT SUBMIT A COMPLICATED / UNCLEAN DESIGN

Industry/Entity Type

Business

Contact Information for Business Card

Dalvik Ostrander Photography

Font styles to use
Other font styles liked:
• Cinzel

Requirements
Must have
• A backpage with nothing but my logo
• Simple design - stands out
Should not have
• Colour that dont align with my logo
• Over complicated '/ non symmetrical design

```html
<!DOCTYPE html>
<html lang="en">
<head>
<meta charset="utf-8">
<title>Dalvik Ostrander Photography — Business Card</title>
<link rel="stylesheet" href="https://fonts.googleapis.com/css2?family=Cinzel:wght@400&display=swap">
<style>
  :root {
    --backdrop: #2a2623;
    --card: #0b0b0b;
    --card-edge: #1a1a1a;
    --gold: #a58d66;
    --gold-soft: #8a7656;
    --icon-disc: #5a5a5a;
  }
  * { margin: 0; padding: 0; box-sizing: border-box; }
  html, body {
    width: 1200px;
    height: 813px;
    overflow: hidden;
    background: var(--backdrop);
  }
  .sheet {
    width: 1200px;
    height: 813px;
    display: flex;
    align-items: center;
    justify-content: center;
    gap: 60px;
    font-family: "Cinzel", serif;
  }
  .card {
    width: 510px;
    height: 292px;
    background: var(--card);
    border: 1px solid var(--card-edge);
    border-radius: 3px;
    position: relative;
    box-shadow: 0 10px 28px rgba(0, 0, 0, 0.45);
  }

  /* Back of card: name mark only */
  .card--back {
    display: flex;
    align-items: center;
    justify-content: center;
  }
  .brand {
    color: var(--gold);
    font-weight: 400;
    text-align: center;
    line-height: 1.1;
  }
  .card--back .brand__name { font-size: 30px; letter-spacing: 1px; }
  .card--back .brand__trade { font-size: 30px; letter-spacing: 9px; margin-top: 4px; }

  /* Front of card: contact details + name mark */
  .card--front {
    display: flex;
    align-items: center;
    justify-content: space-between;
    padding: 0 36px 0 38px;
  }
  .contact-list { list-style: none; }
  .contact-list__item {
    display: flex;
    align-items: center;
    gap: 10px;
    color: var(--gold);
    font-size: 15px;
    letter-spacing: 0.5px;
    margin: 14px 0;
  }
  .contact-list__icon { width: 16px; height: 16px; flex: none; }
  .card--front .brand { color: var(--gold-soft); }
  .card--front .brand__name { font-size: 13px; letter-spacing: 0.5px; }
  .card--front .brand__trade { font-size: 13px; letter-spacing: 4px; margin-top: 2px; }
</style>
</head>
<body>
  <main class="sheet">
    <section class="card card--back" aria-label="Card back">
      <div class="brand">
        <div class="brand__name">Dalvik Ostrander</div>
        <div class="brand__trade">Photography</div>
      </div>
    </section>

    <section class="card card--front" aria-label="Card front">
      <ul class="contact-list">
        <li class="contact-list__item">
          <svg class="contact-list__icon" viewBox="0 0 16 16" aria-hidden="true">
            <circle cx="8" cy="8" r="8" fill="var(--icon-disc)"/>
            <path d="M5.3 4.2l1.3 1.8-.8 1c.5 1 1.2 1.8 2.2 2.3l1-.8 1.8 1.3-.7 1.4c-2.9-.3-5.4-2.8-5.7-5.7z" fill="#111"/>
          </svg>
          <span>07946218350</span>
        </li>
        <li class="contact-list__item">
          <svg class="contact-list__icon" viewBox="0 0 16 16" aria-hidden="true">
            <circle cx="8" cy="8" r="8" fill="var(--icon-disc)"/>
            <circle cx="8" cy="8" r="4.6" fill="none" stroke="#111" stroke-width="1"/>
            <path d="M3.4 8h9.2M8 3.4c-2 2.5-2 6.7 0 9.2M8 3.4c2 2.5 2 6.7 0 9.2" fill="none" stroke="#111" stroke-width="0.9"/>
          </svg>
          <span>tavorelstudio.com</span>
        </li>
        <li class="contact-list__item">
          <svg class="contact-list__icon" viewBox="0 0 16 16" aria-hidden="true">
            <circle cx="8" cy="8" r="8" fill="var(--icon-disc)"/>
            <rect x="4.2" y="5.3" width="7.6" height="5.4" fill="#111"/>
            <path d="M4.4 5.6L8 8.4l3.6-2.8" fill="none" stroke="var(--icon-disc)" stroke-width="0.8"/>
          </svg>
          <span>studio@tavorelstudio.com</span>
        </li>
      </ul>
      <div class="brand">
        <div class="brand__name">Dalvik Ostrander</div>
        <div class="brand__trade">Photography</div>
      </div>
    </section>
  </main>
</body>
</html>
```